Tarrow Consulting Needs Standardised Stationery!

Hello,I am looking at having some standardised stationery to continue building my brand. I am looking for a relatively clean and simple designs using the colours from my logos. Tarrow Consulting is the main business with Quillon Careers Australia a subsidiary.
In particular I am after a design for:
- Letterhead (very important), white background, professional, corporate that I can send to prospective clients. Logo colours.
- Envelope, standard design I can print onto envelopes.
- Pens
- Other stationery/promotional items I can create

Target Market(s)

Universities, government, large organisations.

Industry/Entity Type

Professional Service

Font styles to use
Serif

Requirements
Must have
• Logo, match the design of the Tarrow Consulting logo. Black Quillon Careers Australia logo is a subsidiary.
Should not have
• Too much colour, some colour is good, but I am looking for a clean professional look.

```html
<!DOCTYPE html>
<html lang="en">
<head>
<meta charset="utf-8">
<title>Tarrow Consulting – DL Envelope</title>
<link rel="stylesheet" href="https://fonts.googleapis.com/css2?family=Open+Sans:wght@400;600;700&display=swap">
<style>
  :root {
    --bg: #d9dbe2;
    --paper: #f4f4f4;
    --paper-edge: #e2e2e2;
    --ink: #1f1f1f;
    --mark-faint: #cfcfcf;
    --band-dark: #4a4a4a;
    --band-light: #9a9a9a;
    --flap-dark: #8c8c8c;
    --flap-light: #a9a9a9;
  }
  * { margin: 0; padding: 0; box-sizing: border-box; }
  html, body { width: 1200px; height: 950px; overflow: hidden; }
  body {
    background: var(--bg);
    font-family: "Open Sans", Arial, sans-serif;
    color: var(--ink);
    position: relative;
  }

  .envelope {
    position: absolute;
    left: 200px;
    width: 800px;
    height: 400px;
    background: var(--paper);
    box-shadow: 0 6px 18px rgba(0,0,0,0.12);
    overflow: hidden;
  }
  .envelope--front { top: 40px; }
  .envelope--back { top: 500px; }

  /* front */
  .side-band {
    position: absolute;
    left: 0; top: 0; bottom: 0;
    width: 62px;
    background: linear-gradient(180deg, var(--band-dark) 0%, var(--band-light) 45%, var(--band-dark) 75%, var(--band-light) 100%);
  }
  .sender {
    position: absolute;
    left: 40px;
    top: 42px;
  }
  .sender-logo {
    display: flex;
    align-items: center;
    gap: 10px;
    background: #fff;
    border-radius: 8px;
    padding: 10px 16px 10px 12px;
    box-shadow: 0 1px 3px rgba(0,0,0,0.15);
  }
  .logo-square {
    width: 22px; height: 22px;
    background: var(--ink);
    flex: none;
  }
  .logo-name {
    font-weight: 600;
    font-size: 24px;
    letter-spacing: 1px;
    color: var(--ink);
    line-height: 1;
    white-space: nowrap;
  }
  .sender-address {
    margin-top: 6px;
    font-weight: 700;
    font-size: 13px;
    color: var(--ink);
    white-space: nowrap;
  }
  .subsidiary {
    position: absolute;
    right: 40px;
    top: 40px;
    display: flex;
    align-items: center;
    gap: 14px;
  }
  .subsidiary-circle {
    width: 56px; height: 56px;
    border-radius: 50%;
    background: var(--mark-faint);
    flex: none;
  }
  .subsidiary-name {
    font-size: 19px;
    line-height: 1.15;
    color: var(--mark-faint);
    font-weight: 400;
  }

  /* back */
  .flap {
    position: absolute;
    left: 0; top: 0;
  }
  .fold-lines {
    position: absolute;
    left: 0; top: 0;
  }
  .back-logo {
    position: absolute;
    left: 470px;
    top: 262px;
    display: flex;
    align-items: center;
    gap: 8px;
  }
  .back-logo .logo-square { width: 16px; height: 16px; }
  .back-logo .logo-name { font-size: 18px; }
</style>
</head>
<body>

  <section class="envelope envelope--front" aria-label="Envelope front">
    <div class="side-band" role="img" aria-label="Grey abstract wave pattern band"></div>
    <div class="sender">
      <div class="sender-logo">
        <span class="logo-square"></span>
        <span class="logo-name">Tarrow Consulting</span>
      </div>
      <p class="sender-address">12 Harlow Rd, Westbury, CA 00000</p>
    </div>
    <div class="subsidiary">
      <span class="subsidiary-circle"></span>
      <p class="subsidiary-name">Quillon<br>Careers<br>Australia</p>
    </div>
  </section>

  <section class="envelope envelope--back" aria-label="Envelope back">
    <svg class="fold-lines" width="800" height="400" viewBox="0 0 800 400">
      <path d="M 110 150 Q 100 150 100 170 L 100 400" fill="none" stroke="var(--paper-edge)" stroke-width="2"/>
      <path d="M 690 150 Q 710 150 730 200 L 800 380" fill="none" stroke="var(--paper-edge)" stroke-width="2"/>
    </svg>
    <svg class="flap" width="800" height="400" viewBox="0 0 800 400" role="img" aria-label="Grey geometric pattern on inner flap">
      <defs>
        <linearGradient id="flapFill" x1="0" y1="0" x2="0" y2="1">
          <stop offset="0" stop-color="var(--flap-dark)"/>
          <stop offset="1" stop-color="var(--flap-light)"/>
        </linearGradient>
      </defs>
      <path d="M 0 0 L 800 0 L 800 30 Q 800 55 760 80 L 700 120 Q 680 132 640 132 L 160 132 Q 120 132 80 150 Q 30 172 12 180 Q 0 184 0 160 Z" fill="url(#flapFill)"/>
    </svg>
    <div class="back-logo">
      <span class="logo-square"></span>
      <span class="logo-name">Tarrow Consulting</span>
    </div>
  </section>

</body>
</html>
```